Visitenkarten-Design für Commercial Expert
Zielgruppe
Guten Tag! Ich bin Single und suche neue sportliche Bekannte in der Nähe meines Wohnortes.
Aufgabenstellung
Dr. Mareike Venhaus
Commercial Expert
Telefonnummer 01762290471
Anschrift: Tulpenau 9, 81675 München
https://www.netzvelo-profil.de/profile/Mareike_Venhaus/

```html
<!DOCTYPE html>
<html lang="de">
<head>
<meta charset="utf-8">
<title>Visitenkarte – Dr. Mareike Venhaus</title>
<link href="https://fonts.googleapis.com/css2?family=Questrial&family=Great+Vibes&display=swap" rel="stylesheet">
<style>
  :root {
    --stage: #e6e3e1;
    --card-white: #ffffff;
    --card-fade: #f1f1f1;
    --rose: #cf7fb1;
    --rose-light: #dca2c6;
    --plum-light: #dba3c6;
    --plum-mid: #b9659a;
    --plum-dark: #74265a;
    --ink: #2b2b2b;
    --network-teal: #0f6b6b;
    --script-pink: #f3c6e0;
    --photo-dark: #4f4f4f;
    --photo-mid: #7c6e62;
  }
  * { box-sizing: border-box; margin: 0; padding: 0; }
  html, body { width: 1200px; height: 900px; overflow: hidden; }
  body {
    background: var(--stage);
    font-family: "Questrial", "Century Gothic", sans-serif;
    color: var(--ink);
    position: relative;
  }
  .card {
    position: absolute;
    left: 250px;
    width: 700px;
    height: 400px;
    border-radius: 4px;
    box-shadow: 0 8px 24px rgba(0,0,0,.18);
    overflow: hidden;
  }
  .card-front {
    top: 40px;
    background: linear-gradient(180deg, var(--card-white) 0%, var(--card-fade) 100%);
  }
  .card-back {
    top: 470px;
    background: linear-gradient(110deg, var(--plum-light) 0%, var(--plum-mid) 60%, var(--plum-dark) 100%);
    display: flex;
    align-items: center;
    justify-content: center;
  }
  .portrait {
    position: absolute;
    left: 62px;
    top: 70px;
    width: 210px;
    height: 210px;
    border-radius: 50%;
    background: radial-gradient(circle at 50% 40%, var(--photo-mid) 0%, var(--photo-dark) 70%);
    z-index: 2;
  }
  .identity {
    position: absolute;
    left: 318px;
    top: 64px;
    width: 340px;
  }
  .name {
    color: var(--rose);
    font-size: 27px;
    font-weight: 400;
    letter-spacing: 2px;
    white-space: nowrap;
  }
  .role {
    font-size: 17px;
    letter-spacing: .5px;
    margin-top: 2px;
  }
  .divider {
    height: 1.5px;
    background: var(--rose);
    margin-top: 24px;
    width: 300px;
  }
  .contact-list { list-style: none; margin-top: 24px; }
  .contact-item {
    display: flex;
    align-items: flex-start;
    gap: 14px;
    font-size: 17px;
    letter-spacing: 1.2px;
    line-height: 1.2;
    margin-bottom: 12px;
  }
  .contact-icon { width: 18px; height: 18px; flex: none; margin-top: 3px; fill: var(--rose); }
  .band { position: absolute; background: var(--rose-light); }
  .band-url {
    left: 372px; right: 0; top: 260px; height: 26px;
    background: var(--rose);
    color: #fff;
    font-size: 11.5px;
    letter-spacing: .3px;
    display: flex; align-items: center; padding-left: 12px;
    white-space: nowrap;
  }
  .band-mid { left: 0; width: 282px; top: 292px; height: 22px; }
  .band-base { left: 0; width: 700px; top: 350px; height: 22px; background: linear-gradient(90deg, var(--rose) 0%, var(--rose-light) 100%); }
  .network-label {
    position: absolute;
    left: 292px; top: 280px;
    font-size: 13px;
    letter-spacing: 1px;
    color: var(--network-teal);
  }
  .script-name {
    font-family: "Great Vibes", cursive;
    font-size: 78px;
    color: var(--script-pink);
    letter-spacing: 2px;
  }
</style>
</head>
<body>
  <section class="card card-front">
    <div class="portrait" role="img" aria-label="Porträtfoto von Dr. Mareike Venhaus"></div>
    <div class="identity">
      <h1 class="name">Dr. Mareike Venhaus</h1>
      <p class="role">Commercial Expert</p>
      <div class="divider"></div>
      <ul class="contact-list">
        <li class="contact-item">
          <svg class="contact-icon" viewBox="0 0 24 24" aria-hidden="true"><path d="M12 3 2 12h3v8h5v-5h4v5h5v-8h3z"/></svg>
          <span>Tulpenau 9, 81675 München<br>Germany</span>
        </li>
        <li class="contact-item">
          <svg class="contact-icon" viewBox="0 0 24 24" aria-hidden="true"><path d="M6.6 10.8a15.1 15.1 0 0 0 6.6 6.6l2.2-2.2a1 1 0 0 1 1-.25 11.4 11.4 0 0 0 3.6.57 1 1 0 0 1 1 1V20a1 1 0 0 1-1 1A17 17 0 0 1 3 4a1 1 0 0 1 1-1h3.5a1 1 0 0 1 1 1c0 1.25.2 2.45.57 3.57a1 1 0 0 1-.25 1z"/></svg>
          <span>01762290471</span>
        </li>
      </ul>
    </div>
    <div class="band band-url">www.netzvelo-profil.de/profile/Mareike_Venhaus</div>
    <span class="network-label">NETZVELO</span>
    <div class="band band-mid"></div>
    <div class="band band-base"></div>
  </section>

  <section class="card card-back">
    <p class="script-name">Mareike Venhaus</p>
  </section>
</body>
</html>
```